Namecard Designs+Logo for a High End Automobile Company

We need a new business card for our company called Velta Motorhof.

www.veltamotorhof.example.sg
Our new website will be up in 2.5 months time.

We sell used and brand new continental cars like Korvane, QTL, Dravell, Solbrini and etc. Currently we are operating from 2 offices in Singapore and United Kingdom.

We want a design which is serious. We are open to colours but try to keep it at a maximum of 3 colours.

We prefer something simple and minimal. We are open to 2 sides printing or even 2 sided namecards. Both UK and Singapore company offices address must be in; either side by side, front and back, or even 2 sided cards.

The logo can be a text logo, emblem, abstract, pictorial or combination.

We are printing with Pribo.com so please kindly follow the printing guideline.

http://uk.pribo.example/help/faq/templates-and-guidelines.html

Rich and Car Enthusiasts

Printing

Must have
• Our 2 offices; UK and Singapore.

Our slogan which is " The Automobile Specialist"
Should not have
• Not more than 3 colours

```html
<!DOCTYPE html>
<html lang="en">
<head>
<meta charset="utf-8">
<title>Velta Motorhof – Business Card</title>
<link rel="stylesheet" href="https://fonts.googleapis.com/css2?family=Montserrat:wght@400;600;700&display=swap">
<style>
  :root {
    --ink: #2b2b2e;
    --ink-soft: #6a6a70;
    --accent: #d3201f;
    --paper: #ffffff;
    --stage: #eeeeef;
    --card-dark: #3a3b3f;
    --card-darker: #1f2023;
    --on-dark: #f2f2f2;
  }
  * { box-sizing: border-box; margin: 0; padding: 0; }
  html, body { width: 800px; height: 1200px; overflow: hidden; }
  body {
    background: var(--stage);
    font-family: "Montserrat", Arial, sans-serif;
    color: var(--ink);
    position: relative;
  }

  /* Brand lockup */
  .brand { display: flex; flex-direction: column; align-items: center; }
  .brand-name {
    display: flex; align-items: center; gap: 12px;
    font-weight: 700; letter-spacing: -0.5px; line-height: 1;
    white-space: nowrap;
  }
  .brand-mark { width: 0.42em; height: 0.42em; background: var(--accent); flex: none; }
  .brand-tagline {
    font-weight: 600; letter-spacing: 0.34em; text-transform: uppercase;
    margin-top: 8px; white-space: nowrap;
  }

  .masthead { position: absolute; top: 60px; left: 0; width: 800px; }
  .masthead .brand-name { font-size: 50px; color: var(--ink); }
  .masthead .brand-tagline { font-size: 15px; color: var(--ink); padding-left: 0.34em; }

  /* Cards */
  .card {
    position: absolute; left: 120px; width: 560px; height: 364px;
    box-shadow: 0 6px 20px rgba(0,0,0,0.18);
  }
  .card-front { top: 230px; background: var(--paper); padding: 40px 44px; }
  .card-back {
    top: 650px;
    background: radial-gradient(ellipse at 55% 40%, var(--card-dark), var(--card-darker));
    display: flex; align-items: center; justify-content: center;
  }

  .card-front .brand { align-items: flex-start; }
  .card-front .brand-name { font-size: 34px; gap: 9px; }
  .card-front .brand-tagline { font-size: 10px; margin-top: 5px; }

  .holder { margin-top: 34px; font-size: 14px; }
  .holder-name { font-weight: 700; }
  .holder-role { font-weight: 400; color: var(--ink-soft); margin-left: 6px; }

  .office { margin-top: 12px; font-size: 10.5px; line-height: 1.55; color: var(--ink-soft); }
  .office-city { font-weight: 700; color: var(--ink); }

  .card-web {
    position: absolute; left: 44px; bottom: 30px;
    font-size: 13px; font-weight: 600; color: var(--ink);
  }
  .card-rule {
    position: absolute; left: 44px; right: 44px; bottom: 56px;
    height: 1px; background: #d8d8da;
  }

  .card-back .brand-name { font-size: 40px; color: var(--on-dark); }
  .card-back .brand-tagline { font-size: 12px; color: var(--on-dark); padding-left: 0.34em; }
</style>
</head>
<body>
  <header class="masthead brand">
    <div class="brand-name"><span class="brand-mark"></span>Velta Motorhof</div>
    <div class="brand-tagline">The Automobile Specialist</div>
  </header>

  <section class="card card-front" aria-label="Business card front">
    <div class="brand">
      <div class="brand-name"><span class="brand-mark"></span>Velta Motorhof</div>
      <div class="brand-tagline">The Automobile Specialist</div>
    </div>

    <p class="holder"><span class="holder-name">Mr R Halden</span><span class="holder-role">Director</span></p>

    <div class="office">
      <p><span class="office-city">Singapore:</span> T +65 6200 1100 · E sg@veltamotorhof.example.sg</p>
      <p>12 Harbour View Road, #03-01, Singapore 098765</p>
    </div>
    <div class="office">
      <p><span class="office-city">London:</span> T +44 20 7946 0321 · E uk@veltamotorhof.example.sg</p>
      <p>8 Kensal Mews, London W10 4AB, United Kingdom</p>
    </div>

    <div class="card-rule"></div>
    <p class="card-web">www.veltamotorhof.example.sg</p>
  </section>

  <section class="card card-back" aria-label="Business card back">
    <div class="brand">
      <div class="brand-name"><span class="brand-mark"></span>Velta Motorhof</div>
      <div class="brand-tagline">The Automobile Specialist</div>
    </div>
  </section>
</body>
</html>
```